Advertisement for linkora Ad

We are looking to copy a mailer style design that would normally be sent out to a mailbox. However we have decided to simply use it and run an add on Linkora. please check photo sizes for linkora to make sure your design will work.

also please try to use the colors from our website: brightmeadowclub@postvane.net

we want the same layout as the ad we sent in the files, with different photos and color scheme.

Target Market(s)

dog owners with busy schedules

Font styles to use
Sans Serif

Colors

Designer to choose only greyscale colors for use in the design.

```html
<!DOCTYPE html>
<html lang="en">
<head>
<meta charset="utf-8">
<title>Bright Meadow Canine Club – Daycare Ad</title>
<link href="https://fonts.googleapis.com/css2?family=Jost:wght@400;500;600;700;800&display=swap" rel="stylesheet">
<style>
  :root {
    --page-bg: #f3f3f3;
    --panel-light: #6a6a6a;
    --panel-mid: #474747;
    --panel-dark: #2a2a2a;
    --photo-light: #c4c4c4;
    --photo-mid: #a8a8a8;
    --photo-dark: #8a8a8a;
    --band-black: #0b0b0b;
    --offer-accent: #e4e4e4;
    --white: #ffffff;
    --divider: #d8d8d8;
    --brand-ink: #151515;
  }
  * { box-sizing: border-box; margin: 0; padding: 0; }
  html, body { width: 1031px; height: 1200px; overflow: hidden; }
  body {
    background: var(--page-bg);
    font-family: "Jost", sans-serif;
    position: relative;
  }
  .ad {
    position: absolute;
    left: 36px;
    width: 959px;
    height: 546px;
    background: var(--white);
    box-shadow: 0 6px 22px rgba(0,0,0,0.16);
  }
  .ad--first { top: 40px; }
  .ad--second { top: 616px; }

  .ad__photo {
    position: absolute;
    left: 0; top: 0;
    width: 560px; height: 388px;
    background: linear-gradient(180deg, var(--photo-dark) 0%, var(--photo-light) 22%, var(--photo-mid) 60%, var(--photo-dark) 100%);
  }
  .ad--second .ad__photo {
    background: linear-gradient(180deg, #919191 0%, #c0c0c0 25%, #a9a9a9 65%, #8e8e8e 100%);
  }
  .ad__panel {
    position: absolute;
    left: 0; top: 0;
    width: 959px; height: 388px;
  }
  .brand-mark {
    position: absolute;
    left: 38px; top: 352px;
    display: flex; align-items: center; gap: 7px;
    font-weight: 700; font-size: 15px; letter-spacing: 0.5px;
    color: var(--brand-ink); text-transform: uppercase;
  }
  .brand-mark__dot {
    width: 11px; height: 11px; border-radius: 50%;
    background: var(--brand-ink);
  }

  .pitch {
    position: absolute;
    left: 550px; top: 60px;
    color: var(--white);
  }
  .pitch__headline {
    font-weight: 800; font-size: 36px; line-height: 42px;
    letter-spacing: 0.3px;
  }
  .pitch__list { list-style: none; margin-top: 11px; }
  .pitch__item {
    display: flex; align-items: center; gap: 9px;
    font-weight: 500; font-size: 17.5px; line-height: 30px;
    letter-spacing: 0.3px;
  }
  .pitch__item svg { width: 20px; height: 18px; margin-left: -4px; }
  .pitch__note {
    font-weight: 500; font-size: 13px; letter-spacing: 0.3px;
    padding-left: 25px; margin-top: -3px;
  }
  .pitch__contact {
    margin-top: 10px; padding-left: 6px;
    font-weight: 600; font-size: 19.5px; line-height: 29px;
    letter-spacing: 0.3px;
  }

  .offers {
    position: absolute;
    left: 0; top: 395px;
    width: 959px; height: 151px;
    background: var(--band-black);
  }
  .ad--second .offers {
    background: linear-gradient(180deg, #181818 0%, #141414 50%, #0a0a0a 100%);
  }
  .offer {
    position: absolute;
    top: 26px;
    color: var(--white);
  }
  .offer--daycare { left: 60px; }
  .offer--bath { left: 359px; }
  .offer--groom { left: 679px; }
  .offer__title {
    color: var(--offer-accent);
    font-weight: 700; font-size: 24.5px; line-height: 32px;
    letter-spacing: 0.3px; height: 68px;
  }
  .offer--bath .offer__title { padding-top: 17px; }
  .offer__terms {
    font-size: 11.5px; line-height: 21px; font-weight: 400;
  }
  .offers__divider {
    position: absolute;
    top: 30px; width: 1.5px; height: 92px;
    background: var(--divider);
  }
  .offers__divider--one { left: 323px; }
  .offers__divider--two { left: 629px; }
</style>
</head>
<body>

<section class="ad ad--first">
  <div class="ad__photo" role="img" aria-label="Photo of three dogs sitting in a grassy field"></div>
  <svg class="ad__panel" viewBox="0 0 959 388" aria-hidden="true">
    <defs>
      <linearGradient id="panelGreyA" x1="0" y1="0" x2="0.3" y2="1">
        <stop offset="0" stop-color="#6a6a6a"/>
        <stop offset="0.55" stop-color="#474747"/>
        <stop offset="1" stop-color="#2a2a2a"/>
      </linearGradient>
    </defs>
    <polygon points="483,0 959,0 959,388 526,388" fill="url(#panelGreyA)"/>
  </svg>
  <div class="brand-mark"><span class="brand-mark__dot"></span>Bright Meadow</div>
  <div class="pitch">
    <h1 class="pitch__headline">NOT YOUR TYPICAL<br>DOG DAYCARE</h1>
    <ul class="pitch__list">
      <li class="pitch__item"><svg viewBox="0 0 20 18"><path d="M2 9 L8 16 L18 2" fill="none" stroke="#fff" stroke-width="2.4"/></svg>SAFE, OPEN-PLAY DAYCARE</li>
      <li class="pitch__item"><svg viewBox="0 0 20 18"><path d="M2 9 L8 16 L18 2" fill="none" stroke="#fff" stroke-width="2.4"/></svg>EXERCISE &amp; EDUCATION</li>
      <li class="pitch__item"><svg viewBox="0 0 20 18"><path d="M2 9 L8 16 L18 2" fill="none" stroke="#fff" stroke-width="2.4"/></svg>FUN-FILLED DAYS WITH&nbsp; THEIR BFFF</li>
    </ul>
    <p class="pitch__note">(BEST FURRY FRIEND FOREVER)</p>
    <p class="pitch__contact">Bright Meadow Canine Club<br>418 North Willow Road Maple Grove IA<br>555-014-2837</p>
  </div>
  <div class="offers">
    <div class="offer offer--daycare">
      <h2 class="offer__title">FREE FIRST DAY<br>OF DAYCARE!</h2>
      <p class="offer__terms">*Advanced reservations required<br>*Call by 8/31/20 to schedule your appointment</p>
    </div>
    <div class="offers__divider offers__divider--one"></div>
    <div class="offer offer--bath">
      <h2 class="offer__title">ONE FREE BATH!</h2>
      <p class="offer__terms">*Advanced reservations required<br>*Call by 8/31/20 to schedule your appointment</p>
    </div>
    <div class="offers__divider offers__divider--two"></div>
    <div class="offer offer--groom">
      <h2 class="offer__title">$20 OFF<br>FIRST GROOM</h2>
      <p class="offer__terms">*Advanced reservations required<br>*Call by 8/31/20 to schedule your appointment</p>
    </div>
  </div>
</section>

<section class="ad ad--second">
  <div class="ad__photo" role="img" aria-label="Photo of two dogs sitting close together in a grassy field"></div>
  <svg class="ad__panel" viewBox="0 0 959 388" aria-hidden="true">
    <defs>
      <linearGradient id="panelGreyB" x1="0" y1="0" x2="0.3" y2="1">
        <stop offset="0" stop-color="#6a6a6a"/>
        <stop offset="0.55" stop-color="#474747"/>
        <stop offset="1" stop-color="#2a2a2a"/>
      </linearGradient>
    </defs>
    <polygon points="483,0 959,0 959,388 526,388" fill="url(#panelGreyB)"/>
  </svg>
  <div class="brand-mark"><span class="brand-mark__dot"></span>Bright Meadow</div>
  <div class="pitch">
    <h1 class="pitch__headline">NOT YOUR TYPICAL<br>DOG DAYCARE</h1>
    <ul class="pitch__list">
      <li class="pitch__item"><svg viewBox="0 0 20 18"><path d="M2 9 L8 16 L18 2" fill="none" stroke="#fff" stroke-width="2.4"/></svg>SAFE, OPEN-PLAY DAYCARE</li>
      <li class="pitch__item"><svg viewBox="0 0 20 18"><path d="M2 9 L8 16 L18 2" fill="none" stroke="#fff" stroke-width="2.4"/></svg>EXERCISE &amp; EDUCATION</li>
      <li class="pitch__item"><svg viewBox="0 0 20 18"><path d="M2 9 L8 16 L18 2" fill="none" stroke="#fff" stroke-width="2.4"/></svg>FUN-FILLED DAYS WITH&nbsp; THEIR BFFF</li>
    </ul>
    <p class="pitch__note">(BEST FURRY FRIEND FOREVER)</p>
    <p class="pitch__contact">Bright Meadow Canine Club<br>418 North Willow Road Maple Grove IA<br>555-014-2837</p>
  </div>
  <div class="offers">
    <div class="offer offer--daycare">
      <h2 class="offer__title">FREE FIRST DAY<br>OF DAYCARE!</h2>
      <p class="offer__terms">*Advanced reservations required<br>*Call by 8/31/20 to schedule your appointment</p>
    </div>
    <div class="offers__divider offers__divider--one"></div>
    <div class="offer offer--bath">
      <h2 class="offer__title">ONE FREE BATH!</h2>
      <p class="offer__terms">*Advanced reservations required<br>*Call by 8/31/20 to schedule your appointment</p>
    </div>
    <div class="offers__divider offers__divider--two"></div>
    <div class="offer offer--groom">
      <h2 class="offer__title">$20 OFF<br>FIRST GROOM</h2>
      <p class="offer__terms">*Advanced reservations required<br>*Call by 8/31/20 to schedule your appointment</p>
    </div>
  </div>
</section>

</body>
</html>
```